Business card

We are looking for a creative person to deigns our company business card.

Target Market(s)

College age student

Industry/Entity Type

Accommodation

Contact Information for Business Card

We want a fun, clean and sophisticated design. It should look good, but more importantly the information should be legible.

Font styles to use
Serif
Sans Serif
Other font styles liked:
• Open Sans ,

Colors
33a6d7

Requirements
Must have
• Must have a young and memorable message. Be legible.
• Our logo on the back on a solid blue , please find color and logo attached
• LodgeNestly.com on the back.
Nice to have
• I would like to have couple of different fonts on the LodgeNestly.com on the back of the cards with a solid blue.

```html
<!DOCTYPE html>
<html lang="en">
<head>
<meta charset="UTF-8">
<title>LodgeNestly Business Card</title>
<link href="https://fonts.googleapis.com/css2?family=Montserrat:wght@400;500;600;700&display=swap" rel="stylesheet">
<style>
  :root {
    --brand-blue: #3596d2;
    --deep-blue: #0f5586;
    --paper: #ffffff;
    --ink: #333333;
    --rule: #9a9a9a;
    --backdrop: #9d9d9d;
  }
  * { margin: 0; padding: 0; box-sizing: border-box; }
  html, body {
    width: 1200px; height: 900px; overflow: hidden;
    background: var(--backdrop);
    font-family: "Montserrat", sans-serif;
  }
  .card {
    position: absolute;
    left: 320px;
    width: 560px; height: 320px;
    overflow: hidden;
    box-shadow: 0 6px 18px rgba(0,0,0,0.25);
  }
  .card--front { top: 110px; background: var(--brand-blue); }
  .card--back { top: 470px; background: var(--paper); }

  .front-name {
    position: absolute; left: 0; right: 0; top: 136px;
    text-align: center; color: var(--paper);
    font-weight: 700; font-size: 40px; letter-spacing: -0.5px;
  }

  .back-brand {
    position: absolute; left: 40px; top: 108px; width: 230px;
    display: flex; flex-direction: column; align-items: center; gap: 14px;
  }
  .back-brand__square { width: 42px; height: 42px; background: var(--brand-blue); }
  .back-brand__name {
    color: var(--deep-blue); font-weight: 700; font-size: 30px; letter-spacing: -0.5px;
  }
  .divider {
    position: absolute; left: 290px; top: 50px;
    width: 2px; height: 140px; background: var(--rule);
  }
  .contact { position: absolute; left: 318px; top: 42px; color: var(--ink); }
  .contact__name { color: var(--brand-blue); font-weight: 700; font-size: 25px; line-height: 1.1; }
  .contact__title { font-size: 15px; font-weight: 500; margin-bottom: 14px; }
  .contact__address { font-size: 11.5px; line-height: 1.6; margin-bottom: 10px; }
  .contact__line { display: flex; align-items: center; gap: 8px; font-size: 12.5px; line-height: 1.5; }
  .contact__line svg { width: 12px; height: 12px; fill: var(--brand-blue); flex: none; }

  .wave { position: absolute; left: 0; bottom: 0; width: 560px; height: 110px; }
  .website {
    position: absolute; left: 96px; bottom: 20px;
    color: var(--paper); font-size: 13px; font-weight: 500; letter-spacing: 0.3px;
  }
</style>
</head>
<body>
  <section class="card card--front">
    <div class="front-name">LodgeNestly</div>
  </section>

  <section class="card card--back">
    <div class="back-brand">
      <span class="back-brand__square"></span>
      <span class="back-brand__name">LodgeNestly</span>
    </div>

    <div class="divider"></div>

    <div class="contact">
      <div class="contact__name">Daniel Reyes</div>
      <div class="contact__title">President</div>
      <div class="contact__address">Level 2, 17 Harbour Lane<br>Carlton, VIC 3053</div>
      <div class="contact__line">
        <svg viewBox="0 0 24 24"><path d="M6.6 10.8a15 15 0 0 0 6.6 6.6l2.2-2.2a1 1 0 0 1 1-.25 11.4 11.4 0 0 0 3.6.6 1 1 0 0 1 1 1V20a1 1 0 0 1-1 1A17 17 0 0 1 3 4a1 1 0 0 1 1-1h3.5a1 1 0 0 1 1 1c0 1.25.2 2.45.6 3.6a1 1 0 0 1-.25 1z"/></svg>
        555 210 4478
      </div>
      <div class="contact__line">
        <svg viewBox="0 0 24 24"><path d="M7 1h10a2 2 0 0 1 2 2v18a2 2 0 0 1-2 2H7a2 2 0 0 1-2-2V3a2 2 0 0 1 2-2zm0 3v14h10V4zm5 15.5a1 1 0 1 0 0 2 1 1 0 0 0 0-2z"/></svg>
        555 390 1126
      </div>
      <div class="contact__line">
        <svg viewBox="0 0 24 24"><path d="M2 5h20v2l-10 6L2 7zm0 4.3 10 6 10-6V19H2z"/></svg>
        hello@lodgenestly.com
      </div>
    </div>

    <svg class="wave" viewBox="0 0 560 110" preserveAspectRatio="none" aria-hidden="true">
      <path d="M0 52 C120 18 230 28 330 40 C420 50 500 30 560 8 L560 110 L0 110 Z" fill="var(--brand-blue)"/>
      <path d="M0 68 C120 30 230 36 330 46 C420 55 500 38 560 20 L560 110 L0 110 Z" fill="var(--paper)"/>
      <path d="M0 74 C120 38 230 42 330 50 C420 58 500 42 560 26 L560 110 L0 110 Z" fill="var(--deep-blue)"/>
    </svg>
    <div class="website">www.lodgenestly.com</div>
  </section>
</body>
</html>
```